Lumo4Kart - a fintech company - business card

We need a business card design for our Payments Technology company in Sydney, Australia. We provide business with payment solutions expanding across EFTPOS machines, online payment gateways and mobile payment solutions. We would like to see designs that are clean, classy and professional.
Target Market(s)
Business professionals, executives, c-suite
Industry/Entity Type
Fintech
Contact Information for Business Card
Will be on 400gsm. Logo will most likely be spot gloss unless designer recommends otherwise.
Font styles to use
Sans Serif
Requirements
Must have
- We need our website (lumo4kart.com.au), email (contact@lumo4kart.com.au), mobile (0432 587 904) and direct phone number (02 6815 3927) to feature on the card along with our logo (attached) and the words "EFTPOS | ONLINE | MOBILE"
- Font = Roboto

```html
<!DOCTYPE html>
<html lang="en">
<head>
<meta charset="utf-8">
<title>Lumo4Kart business card</title>
<link rel="stylesheet" href="https://fonts.googleapis.com/css2?family=Oswald:wght@500&family=Roboto:wght@400;500;700&display=swap">
<style>
  :root {
    --bg: #2a2c2f;
    --card-white: #ffffff;
    --card-shade: #eceeef;
    --brand-blue: #1a5a8c;
    --brand-blue-dark: #124570;
    --brand-blue-light: #1d6aa3;
    --ink: #3a3d40;
    --ink-soft: #55595d;
    --mark-light: #d9dde2;
    --faint-circle: #e3e9f1;
  }
  * { margin: 0; padding: 0; box-sizing: border-box; }
  html, body { width: 1200px; height: 900px; overflow: hidden; }
  body {
    background: var(--bg);
    font-family: "Roboto", sans-serif;
    position: relative;
  }
  .card {
    position: absolute;
    left: 285px;
    width: 630px;
    height: 360px;
    border-radius: 18px;
    overflow: hidden;
    box-shadow: 0 10px 28px rgba(0,0,0,0.45);
  }
  .card-front {
    top: 60px;
    background: radial-gradient(ellipse at 60% 35%, var(--card-white) 40%, var(--card-shade) 100%);
  }
  .card-back {
    top: 480px;
    background: linear-gradient(160deg, var(--brand-blue-light) 0%, var(--brand-blue) 50%, var(--brand-blue-dark) 100%);
    display: flex;
    align-items: center;
    justify-content: center;
    gap: 22px;
  }
  .faint-circle {
    position: absolute;
    left: 235px;
    top: 95px;
    width: 190px;
    height: 190px;
    border-radius: 50%;
    background: var(--faint-circle);
  }
  .identity {
    position: absolute;
    left: 70px;
    top: 118px;
    width: 230px;
    text-align: right;
  }
  .person-name {
    font-family: "Oswald", sans-serif;
    font-weight: 500;
    font-size: 38px;
    letter-spacing: 1px;
    color: var(--brand-blue);
    text-transform: uppercase;
    line-height: 1;
  }
  .person-role {
    font-size: 15px;
    font-weight: 500;
    color: var(--ink-soft);
    margin-top: 4px;
  }
  .divider {
    position: absolute;
    left: 318px;
    top: 115px;
    width: 2px;
    height: 80px;
    background: var(--brand-blue);
  }
  .contact-list {
    position: absolute;
    left: 340px;
    top: 160px;
    list-style: none;
  }
  .contact-item {
    display: flex;
    align-items: center;
    gap: 9px;
    font-size: 17px;
    font-weight: 500;
    color: var(--ink);
    line-height: 24px;
  }
  .contact-icon { width: 12px; height: 12px; flex: none; }
  .service-line {
    position: absolute;
    left: 60px;
    bottom: 34px;
    font-size: 15px;
    font-weight: 500;
    letter-spacing: 0.5px;
    color: var(--ink);
  }
  .brand-dot {
    width: 110px;
    height: 110px;
    border-radius: 50%;
    background: var(--mark-light);
  }
  .brand-name {
    font-family: "Roboto", sans-serif;
    font-weight: 700;
    font-size: 58px;
    letter-spacing: 2px;
    color: var(--mark-light);
    text-transform: uppercase;
  }
</style>
</head>
<body>
  <section class="card card-front" aria-label="Business card front">
    <div class="faint-circle"></div>
    <div class="identity">
      <div class="person-name">Dana Whitlow</div>
      <div class="person-role">Director</div>
    </div>
    <div class="divider"></div>
    <ul class="contact-list">
      <li class="contact-item">
        <svg class="contact-icon" viewBox="0 0 12 12"><rect x="3" y="0.5" width="6" height="11" rx="1.2" fill="none" stroke="#1a5a8c" stroke-width="1.3"/><circle cx="6" cy="9.5" r="0.7" fill="#1a5a8c"/></svg>
        0432 587 904
      </li>
      <li class="contact-item">
        <svg class="contact-icon" viewBox="0 0 12 12"><path d="M2.5 1 L4.5 1 L5.3 3.6 L4 4.6 C4.6 6 5.8 7.3 7.4 8 L8.4 6.7 L11 7.5 L11 9.5 C11 10.4 10.2 11 9.3 11 C5 10.6 1.4 7 1 2.7 C1 1.8 1.6 1 2.5 1 Z" fill="#1a5a8c"/></svg>
        02 6815 3927
      </li>
      <li class="contact-item">
        <svg class="contact-icon" viewBox="0 0 12 12"><rect x="0.7" y="2.2" width="10.6" height="7.6" rx="0.8" fill="none" stroke="#1a5a8c" stroke-width="1.2"/><path d="M1 2.6 L6 6.6 L11 2.6" fill="none" stroke="#1a5a8c" stroke-width="1.2"/></svg>
        contact@lumo4kart.com.au
      </li>
      <li class="contact-item">
        <svg class="contact-icon" viewBox="0 0 12 12"><circle cx="6" cy="6" r="5.2" fill="none" stroke="#1a5a8c" stroke-width="1.1"/><ellipse cx="6" cy="6" rx="2.2" ry="5.2" fill="none" stroke="#1a5a8c" stroke-width="1"/><path d="M0.8 6 H11.2 M1.6 3.4 H10.4 M1.6 8.6 H10.4" stroke="#1a5a8c" stroke-width="0.9"/></svg>
        www.lumo4kart.com.au
      </li>
    </ul>
    <div class="service-line">EFTPOS | ONLINE | MOBILE</div>
  </section>

  <section class="card card-back" aria-label="Business card back">
    <div class="brand-dot"></div>
    <div class="brand-name">Lumo4Kart</div>
  </section>
</body>
</html>
```